Zielgruppe
brinko handel ist eine Vertriebsagentur, die sich ausschließlich auf den BtoB Vertrieb spezialisiert hat. Wir agieren seit 19 Jahren am Markt und sind mehrfach ausgezeichneter Exzellenzberater des Mittelstandes. Wir unterstützen mittelständische Unternehmen, Familienunternehmen, Start up´s in der Wachstumsphase und Großkonzerne in der Industrie und im Dienstleistungsbereich. Ansprechpartner für uns sind Vertriebsleiter und GF´s in den Unternehmen.
Aufgabenstellung
Wir möchten unsere Angebotsvorlage neu im Layout neu designen lassen. Sie soll unsere Arbeitsweise zielgenau - authentisch - pfiffig widerspiegeln. Ich möchte gerne eine moderne und klare Struktur. Auf einer Seite sollen unsere USP´s dargestellt werden und auf ein - zwei Seiten ist das Angebot - in den folgenden Seiten sind die Vertragsinhalte.

```html
<!DOCTYPE html>
<html lang="de">
<head>
<meta charset="utf-8">
<title>brinko handel – Angebotsvorlage</title>
<link href="https://fonts.googleapis.com/css2?family=Arimo:wght@400;700&display=swap" rel="stylesheet">
<style>
  :root {
    --backdrop: #e4e4e4;
    --paper: #f4f4f4;
    --brand-blue: #1f3f8a;
    --accent-red: #e2482e;
    --ink: #2b2b2b;
    --ink-soft: #4a4a4a;
    --tile: #dadada;
    --rule: #d2d2d2;
  }
  * { box-sizing: border-box; margin: 0; padding: 0; }
  html, body { width: 1200px; height: 1200px; overflow: hidden; }
  body {
    background: var(--backdrop);
    font-family: "Arimo", Arial, sans-serif;
    color: var(--ink);
    position: relative;
  }
  .page {
    position: absolute;
    top: 218px;
    width: 540px;
    height: 764px;
    background: var(--paper);
    overflow: hidden;
  }
  .page--advantages { left: 40px; }
  .page--cover { left: 620px; }

  .offer-number {
    position: absolute;
    font-size: 9px;
    font-weight: 700;
    color: var(--accent-red);
  }
  .header-rule {
    position: absolute;
    height: 3px;
    background: var(--rule);
  }
  .page--advantages .offer-number { left: 27px; top: 30px; }
  .page--advantages .header-rule { left: 27px; right: 27px; top: 50px; }

  .advantages-title {
    position: absolute;
    left: 0; right: 0; top: 112px;
    text-align: center;
    font-size: 26px;
    font-weight: 700;
    color: var(--brand-blue);
  }
  .title-bar {
    position: absolute;
    left: 120px; width: 310px; top: 168px;
    height: 3px;
    background: var(--ink-soft);
  }

  .advantage-grid {
    position: absolute;
    left: 38px; top: 228px;
    display: grid;
    grid-template-columns: repeat(4, 113px);
    grid-template-rows: repeat(2, 218px);
    gap: 14px 8px;
  }
  .advantage {
    background: var(--tile);
    padding: 11px 5px 0;
    text-align: center;
    overflow: hidden;
  }
  .advantage__icon {
    width: 42px; height: 42px;
    display: block;
    margin: 0 auto 10px;
  }
  .advantage__title {
    font-size: 10.5px;
    font-weight: 700;
    color: var(--ink-soft);
    text-transform: uppercase;
    line-height: 1.2;
    min-height: 26px;
    display: flex;
    align-items: center;
    justify-content: center;
    margin-bottom: 4px;
  }
  .advantage__text {
    font-size: 7.9px;
    line-height: 1.36;
    color: var(--ink-soft);
    hyphens: auto;
  }

  .footer-rule {
    position: absolute;
    left: 27px; right: 27px;
    height: 2px;
    background: var(--rule);
  }
  .contact-line {
    position: absolute;
    left: 27px; right: 27px;
    font-size: 8.4px;
    color: var(--ink);
    white-space: nowrap;
  }
  .page--advantages .footer-rule { top: 724px; }
  .page--advantages .contact-line { top: 735px; }

  /* Cover page */
  .cover-photo {
    position: absolute;
    left: 0; top: 0;
    width: 540px; height: 764px;
  }
  .page--cover .offer-number { right: 26px; top: 30px; }
  .page--cover .header-rule { left: 35px; right: 26px; top: 51px; background: #ffffff; opacity: .85; }
  .cover-headline {
    position: absolute;
    left: 219px; top: 355px;
    font-size: 53px;
    line-height: 1.02;
    font-weight: 400;
    color: var(--brand-blue);
    text-transform: uppercase;
    letter-spacing: -.6px;
  }
  .about-heading {
    position: absolute;
    left: 174px; top: 618px;
    font-size: 16px;
    font-weight: 700;
    color: var(--ink);
  }
  .about-intro {
    position: absolute;
    left: 174px; top: 648px;
    width: 172px;
    font-size: 8px;
    line-height: 2.15;
    color: var(--ink);
    white-space: nowrap;
  }
  .about-text {
    position: absolute;
    left: 354px; top: 538px;
    width: 166px;
    font-size: 8px;
    line-height: 1.5;
    color: var(--ink);
  }
  .about-text p + p { margin-top: 9px; }
  .page--cover .footer-rule { left: 35px; right: 26px; top: 726px; }
  .page--cover .contact-line { left: 35px; top: 736px; }
</style>
</head>
<body>

<section class="page page--advantages">
  <div class="offer-number">Angebot-Nr. 20221008</div>
  <div class="header-rule"></div>

  <h1 class="advantages-title">Ihre Vorteile</h1>
  <div class="title-bar"></div>

  <div class="advantage-grid">
    <article class="advantage">
      <svg class="advantage__icon" viewBox="0 0 44 44" aria-hidden="true">
        <circle cx="22" cy="22" r="19.5" fill="#fff" stroke="#1f3f8a" stroke-width="3"/>
        <path d="M16 14c1.5-1 3 2 3.5 3.5.3 1-1.5 1.8-1.2 2.8.8 2 2.5 3.8 4.5 4.7 1 .3 1.8-1.5 2.8-1.2 1.5.5 4.5 2 3.5 3.5-1 1.5-2.5 2.5-4.5 2-5-1.2-9.5-5.7-10.7-10.7-.5-2 .6-3.6 2.1-4.6z" fill="none" stroke="#2b2b2b" stroke-width="1.4"/>
        <path d="M24 14a6 6 0 0 1 6 6M24 17a3 3 0 0 1 3 3" fill="none" stroke="#2b2b2b" stroke-width="1.3"/>
      </svg>
      <h2 class="advantage__title">Entscheider</h2>
      <p class="advantage__text">Wir führen 12.000 Gespräche im Monat mit Vorständen, Geschäfts&shy;führern, Marketing-, Vertriebs- und Einkaufsleitern</p>
    </article>

    <article class="advantage">
      <svg class="advantage__icon" viewBox="0 0 44 44" aria-hidden="true">
        <circle cx="22" cy="22" r="19.5" fill="#fff" stroke="#1f3f8a" stroke-width="3"/>
        <rect x="13.5" y="15" width="17" height="15" rx="1.5" fill="none" stroke="#2b2b2b" stroke-width="1.4"/>
        <path d="M13.5 19.5h17M17.5 13v4M26.5 13v4" stroke="#2b2b2b" stroke-width="1.4"/>
        <rect x="17" y="23" width="3" height="3" fill="#2b2b2b"/>
      </svg>
      <h2 class="advantage__title">Richtiger Zeitpunkt</h2>
      <p class="advantage__text">Wir haben das Fingerspitz&shy;engefühl beim Interessent&shy;en zum richtigen Zeitpunkt der Entscheidung präsent zu sein, ohne penetrant zu wirken</p>
    </article>

    <article class="advantage">
      <svg class="advantage__icon" viewBox="0 0 44 44" aria-hidden="true">
        <circle cx="22" cy="22" r="19.5" fill="#fff" stroke="#1f3f8a" stroke-width="3"/>
        <rect x="13" y="13" width="12" height="9" fill="none" stroke="#2b2b2b" stroke-width="1.3"/>
        <path d="M15 20l3-3 2 2 3-3" fill="none" stroke="#2b2b2b" stroke-width="1.2"/>
        <circle cx="27" cy="25" r="2.3" fill="none" stroke="#2b2b2b" stroke-width="1.3"/>
        <path d="M23 31c0-3 2-4 4-4s4 1 4 4" fill="none" stroke="#2b2b2b" stroke-width="1.3"/>
        <circle cx="17" cy="27" r="1.8" fill="none" stroke="#2b2b2b" stroke-width="1.2"/>
        <path d="M14 32c0-2 1.5-3 3-3s3 1 3 3" fill="none" stroke="#2b2b2b" stroke-width="1.2"/>
      </svg>
      <h2 class="advantage__title">Vertriebsaffin</h2>
      <p class="advantage__text">Kompetenz und vor allem Erfahrungen im Vertrieb lassen uns schnell und zielsicher für Sie agieren. Wir wissen wie wir die richtigen Ansprechpartner kontaktieren und auch begeistern können.</p>
    </article>

    <article class="advantage">
      <svg class="advantage__icon" viewBox="0 0 44 44" aria-hidden="true">
        <circle cx="22" cy="22" r="19.5" fill="#fff" stroke="#1f3f8a" stroke-width="3"/>
        <rect x="14" y="14" width="16" height="16" rx="1" fill="none" stroke="#2b2b2b" stroke-width="1.4"/>
        <circle cx="22" cy="22" r="4" fill="none" stroke="#2b2b2b" stroke-width="1.4"/>
        <circle cx="22" cy="22" r="1.3" fill="#2b2b2b"/>
        <path d="M17 17h2M25 27h2" stroke="#2b2b2b" stroke-width="1.2"/>
      </svg>
      <h2 class="advantage__title">Technikkom&shy;petenz</h2>
      <p class="advantage__text">Durch unser technisches Interesse und die Möglich&shy;keit, die wichtigsten Faktoren in der Akquise und den Ansprechpartner zu identifizieren, können wir auch in komplexen technischen Projekten agieren.</p>
    </article>

    <article class="advantage">
      <svg class="advantage__icon" viewBox="0 0 44 44" aria-hidden="true">
        <circle cx="22" cy="22" r="19.5" fill="#fff" stroke="#1f3f8a" stroke-width="3"/>
        <rect x="15" y="20.5" width="14" height="11" rx="1.5" fill="none" stroke="#2b2b2b" stroke-width="1.4"/>
        <path d="M18 20.5v-3a4 4 0 0 1 8 0v3" fill="none" stroke="#2b2b2b" stroke-width="1.4"/>
        <circle cx="22" cy="26" r="1.3" fill="#2b2b2b"/>
      </svg>
      <h2 class="advantage__title">Vertrauen</h2>
      <p class="advantage__text">Ihre Kundendaten sind bei uns in sicheren Händen. Wir arbeiten auf eigenen Servern die täglich 2-fach gesichert werden. Eine Verschwiegenheits&shy;erklärung nach dem DGSVO ist für uns selbst&shy;verständlich!</p>
    </article>

    <article class="advantage">
      <svg class="advantage__icon" viewBox="0 0 44 44" aria-hidden="true">
        <circle cx="22" cy="22" r="19.5" fill="#fff" stroke="#1f3f8a" stroke-width="3"/>
        <circle cx="22" cy="21" r="9" fill="none" stroke="#2b2b2b" stroke-width="1.4"/>
        <circle cx="22" cy="21" r="5.5" fill="none" stroke="#2b2b2b" stroke-width="1.3"/>
        <circle cx="22" cy="19.5" r="1.6" fill="#2b2b2b"/>
        <path d="M19 25c.5-2 1.5-3 3-3s2.5 1 3 3" fill="none" stroke="#2b2b2b" stroke-width="1.2"/>
      </svg>
      <h2 class="advantage__title">Volle Konzentration</h2>
      <p class="advantage__text">Unsere Mitarbeiter sind alle Muttersprachler, arbeiten in einzelnen Büros –kein Homeoffice- für eine ruhige Atmosphäre und optimale Konzentration. Unser Sitz ist in Deutschland.</p>
    </article>

    <article class="advantage">
      <svg class="advantage__icon" viewBox="0 0 44 44" aria-hidden="true">
        <circle cx="22" cy="22" r="19.5" fill="#fff" stroke="#1f3f8a" stroke-width="3"/>
        <rect x="15" y="14.5" width="14" height="17" rx="1.5" fill="none" stroke="#2b2b2b" stroke-width="1.4"/>
        <rect x="19" y="12.5" width="6" height="3.5" rx="1" fill="#fff" stroke="#2b2b2b" stroke-width="1.3"/>
        <path d="M18.5 23l2.5 2.5 4.5-5" fill="none" stroke="#2b2b2b" stroke-width="1.5"/>
      </svg>
      <h2 class="advantage__title">Qualität</h2>
      <p class="advantage__text">Unsere Team wird per&shy;manent geschult durch Team- und Einzelcoach&shy;ing. Es finden regelmäßig Projektbesprechungen statt. Dabei wird auch der Akquiseprozess belebt und das Gesprächskonzept flexibel angepasst.</p>
    </article>

    <article class="advantage">
      <svg class="advantage__icon" viewBox="0 0 44 44" aria-hidden="true">
        <circle cx="22" cy="22" r="19.5" fill="#fff" stroke="#1f3f8a" stroke-width="3"/>
        <circle cx="22" cy="22" r="9" fill="none" stroke="#2b2b2b" stroke-width="1.5"/>
        <path d="M22 13v9h9" fill="none" stroke="#2b2b2b" stroke-width="1.5"/>
      </svg>
      <h2 class="advantage__title">No Limit</h2>
      <p class="advantage__text">Unsere Gespräche sind nicht zeitlich begrenzt. Der Gesprächspartner bestimmt den Zeitpunkt der erneuten Kontaktaufnahme und die Gesprächsdauer. Qualität vor Quantität ist unser Prinzip!</p>
    </article>
  </div>

  <div class="footer-rule"></div>
  <p class="contact-line">Marlen Voss-Albrecht &nbsp;| &nbsp;+49 (0) 170 482 316 7 &nbsp;| &nbsp;mva@brinko-handel.de &nbsp;| &nbsp;Lindenweg 7 &nbsp;| &nbsp;90402 Nürnberg &nbsp;| &nbsp;0911 634 208 0</p>
</section>

<section class="page page--cover">
  <svg class="cover-photo" viewBox="0 0 488 688" preserveAspectRatio="none" role="img" aria-label="Porträtfoto der Geschäftsführerin in roter Jacke, die mit ausgestreckter Hand auf den Betrachter zeigt, vor warm beleuchtetem Innenraum">
    <defs>
      <linearGradient id="photoTone" x1="0" y1="0" x2="0.4" y2="1">
        <stop offset="0" stop-color="#3a2a22"/>
        <stop offset="0.35" stop-color="#8a5a3a"/>
        <stop offset="0.62" stop-color="#c0562f"/>
        <stop offset="1" stop-color="#d8432a"/>
      </linearGradient>
      <clipPath id="photoArc">
        <circle cx="82" cy="243" r="300"/>
      </clipPath>
    </defs>
    <rect x="0" y="0" width="488" height="688" fill="url(#photoTone)" clip-path="url(#photoArc)"/>
  </svg>

  <div class="offer-number">Angebot-Nr. 20221008</div>
  <div class="header-rule"></div>

  <h1 class="cover-headline">Neue<br>Märkte<br>erobern</h1>

  <h2 class="about-heading">Wer wir sind?</h2>
  <p class="about-intro">brinko handel – seit 19 Jahren am Markt –<br>hat sich auf die Kaltakquise und den Vertrieb<br>im &nbsp;BtoB-Bereich spezialisiert –</p>

  <div class="about-text">
    <p>Wir sind der Turbo für Ihren Vertrieb und gehören zu den 10 führenden Anbietern im B2B-Vertrieb. Wir bewegen uns sicher in der Akquise in der oberen Führungsebene bis zum DAX-Konzern. Wir bieten eine 720°strukturierte Vertriebsberatung, -umsetzung und –kontrolle: von A (Analyse) – Z (Verkauf). Wir denken vor und zurück, reflektieren Gespräche und Zielgruppe.</p>
    <p>Wir sind zum 3. Mal in Folge als Exzellenzberater Deutscher Mittelstand im Vertrieb ausgezeichnet!</p>
  </div>

  <div class="footer-rule"></div>
  <p class="contact-line">Marlen Voss-Albrecht &nbsp;| &nbsp;+49 (0) 170 482 316 7 &nbsp;| &nbsp;mva@brinko-handel.de &nbsp;| &nbsp;Lindenweg 7 &nbsp;| &nbsp;90402 Nürnberg &nbsp;| &nbsp;0911 634 208 0</p>
</section>

</body>
</html>
```